skin elixir serum with snail extract

I am working at a natural skincare company. We are going to launch a new product - a skin serum. completely natural, super concentrated, multi use (face, neck , eyes). But we need the packaging (box and bottle label) to be aligned to our brand's philosophy, design etc. (See more at pindomare.com)

Here's a more detailed description :
"Elevate your skincare routine with Brusquel Elixir, the ultimate one-drop wonder enriched with potent snail secretion. Experience the magic as our 100% natural serum transforms your face, eyes, décolleté, and neck. Get ready to say Wow to a new level of radiance!"

Target Market(s)

natural skincare enthusiasts - beauty pioneers

Industry/Entity Type

beauty - wellness

Requirements
Nice to have
• based on the overall brand philosophy (see pindomare.com)

```html
<!DOCTYPE html>
<html lang="en">
<head>
<meta charset="utf-8">
<title>Pindomare Skin Elixir Serum – Box Dieline and Bottle Label</title>
<link rel="stylesheet" href="https://fonts.googleapis.com/css2?family=Poppins:wght@400;600&display=swap">
<style>
  :root {
    --paper: #fafafa;
    --plum: #7b0a46;
    --label-plum: #7c0843;
    --magenta: #c6379a;
    --lace: #a85d8f;
    --white: #ffffff;
    --ink-plum: #7b0a46;
  }
  * { margin: 0; padding: 0; box-sizing: border-box; }
  html, body { width: 1200px; height: 903px; overflow: hidden; background: var(--paper); }
  body { position: relative; font-family: "Poppins", Arial, sans-serif; color: var(--white); }

  .dieline { position: absolute; left: 0; top: 0; width: 1200px; height: 903px; }

  .brand-name { position: absolute; text-align: center; font-family: "Poppins", Arial, sans-serif; font-weight: 400; font-size: 21px; letter-spacing: 1px; line-height: 1; }

  .side-copy { position: absolute; width: 124px; font-size: 8.3px; line-height: 12px; }
  .side-copy p { margin-bottom: 11px; }
  .side-copy .bold { font-weight: 600; }
  .side-copy .gap { margin-top: 15px; }

  .front-info { position: absolute; left: 388px; width: 147px; text-align: center; }
  .product-name { font-size: 10.5px; line-height: 14px; letter-spacing: .3px; top: 464px; }
  .product-uses { font-size: 8px; letter-spacing: .4px; top: 510px; }
  .product-claim { font-size: 7.5px; line-height: 10px; top: 536px; }
  .product-volume { font-size: 7.5px; line-height: 11px; top: 577px; }
  .product-volume strong { font-weight: 600; }

  .label-copy { position: absolute; left: 916px; width: 102px; text-align: center; color: var(--ink-plum); }
  .label-brand { top: 456px; font-size: 15px; letter-spacing: .5px; }
  .label-name { top: 506px; font-size: 8px; line-height: 11px; font-weight: 600; }
  .label-uses { top: 539px; font-size: 6px; letter-spacing: .3px; }
  .label-claim { top: 558px; font-size: 5.5px; line-height: 8px; }
  .label-volume { top: 591px; font-size: 5.5px; line-height: 8px; }
  .label-volume strong { font-weight: 600; }
</style>
</head>
<body>

<svg class="dieline" viewBox="0 0 1200 903" xmlns="http://www.w3.org/2000/svg">
  <!-- left side panel with flaps -->
  <path role="img" aria-label="Lace-style decorative pattern on the left dust flap" fill="var(--lace)" d="M264 172 H385 V285 H264 Z"/>
  <path role="img" aria-label="Lace-style decorative pattern on the left glue strip" fill="var(--lace)" d="M240 265 L196 285 V628 L216 648 H240 Z"/>
  <path role="img" aria-label="Lace-style decorative pattern on the left side panel" fill="var(--lace)" d="M240 265 H388 V648 H240 Z"/>
  <path role="img" aria-label="Lace-style decorative pattern on the lower left flap" fill="var(--lace)" d="M264 628 H385 V740 H264 Z"/>
  <rect class="side-box" x="240" y="285" width="148" height="343" fill="var(--magenta)"/>

  <!-- front panel and top tuck -->
  <rect role="img" aria-label="Front panel and top tuck flap in plum with a faint tonal lace pattern" x="388" y="76" width="147" height="572" fill="var(--plum)"/>

  <!-- right side panel with flaps -->
  <path role="img" aria-label="Lace-style decorative pattern on the right dust flap" fill="var(--lace)" d="M540 172 H660 V265 H540 Z"/>
  <path role="img" aria-label="Lace-style decorative pattern on the right side panel" fill="var(--lace)" d="M535 262 H685 V648 H535 Z"/>
  <path role="img" aria-label="Lace-style decorative pattern on the lower right flap" fill="var(--lace)" d="M540 628 H660 V740 H540 Z"/>
  <rect class="side-box" x="537" y="285" width="148" height="343" fill="var(--magenta)"/>

  <!-- back panel -->
  <rect role="img" aria-label="Back panel in plum with a faint tonal lace pattern" x="685" y="265" width="150" height="570" fill="var(--plum)"/>

  <!-- bottle label -->
  <path fill="var(--white)" stroke="#e6e6e6" stroke-width="1" d="M916 307 H1018 V612 Q1018 622 1008 622 H926 Q916 622 916 612 Z"/>
  <rect x="916" y="307" width="102" height="118" fill="var(--label-plum)"/>
</svg>

<!-- top tuck flap -->
<div class="brand-name" style="left:388px; top:158px; width:147px;">Pindomare</div>

<!-- left side copy -->
<div class="side-copy" style="left:251px; top:310px;">
  <p>Lorem Ipsum is simply dummy text of the printing and typesetting industry. Lorem Ipsum has been the industry's standard dummy text ever since the 1500s</p>
  <p class="bold">Lorem Ipsum is simply dummy text of the printing and typesetting industry.</p>
  <p class="gap">Lorem Ipsum is simply dummy text of the printing and typesetting industry. Lorem Ipsum has been the industry's standard dummy text ever since the 1500s</p>
  <p class="bold gap">Lorem Ipsum is simply dummy text of the printing</p>
  <p class="bold">dummy text of the printing</p>
</div>

<!-- front panel -->
<div class="brand-name" style="left:388px; top:396px; width:147px;">Pindomare</div>
<div class="front-info product-name">SKIN<br>ELIXIR SERUM</div>
<div class="front-info product-uses">FACE &nbsp;I&nbsp; NECK &nbsp;I&nbsp; EYE</div>
<div class="front-info product-claim">completely natural, super<br>concentrated, multi use</div>
<div class="front-info product-volume">Natural Serum<br><strong>30ml</strong></div>

<!-- right side copy -->
<div class="side-copy" style="left:549px; top:310px;">
  <p>Lorem Ipsum is simply dummy text of the printing and typesetting industry. Lorem Ipsum has been the industry's standard dummy text ever since the 1500s</p>
  <p class="bold">Lorem Ipsum is simply dummy text of the printing and typesetting industry.</p>
  <p class="gap">Lorem Ipsum is simply dummy text of the printing and typesetting industry. Lorem Ipsum has been the industry's standard dummy text ever since the 1500s</p>
  <p class="bold gap">Lorem Ipsum is simply dummy text of the printing</p>
  <p class="bold">dummy text of the printing</p>
</div>

<!-- back panel -->
<div class="brand-name" style="left:685px; top:440px; width:150px;">Pindomare</div>

<!-- bottle label -->
<div class="label-copy brand-name label-brand">Pindomare</div>
<div class="label-copy label-name">SKIN<br>ELIXIR SERUM</div>
<div class="label-copy label-uses">FACE &nbsp;I&nbsp; NECK &nbsp;I&nbsp; EYE</div>
<div class="label-copy label-claim">completely natural, super<br>concentrated, multi use</div>
<div class="label-copy label-volume">Natural Serum<br><strong>30ml</strong></div>

</body>
</html>
```